Expanding into international markets & need a new web design

This website is for our products called "Polanexa". They are gel-ice packs that are used to keep other products cold or frozen. Commonly used for seafood, meat, vaccines and produce. We have recently started selling these products in the UK & Australia so need to upgrade our website to look more professional & modern.
Please use our main company colors are #1F419B & #2F4F4F.
Main product selling points that could be featured:
- KBRIL & OPC approved
- Keeps products chilled for longer
- Reuseable & economical
There is no online shop required at the moment, the website is just an online catalogue to promote the products and get international distributor contact information.
Just home page layout design is required at the moment.
Our existing website is www.polanexa.example where you can find more information, our logo & pictures.
Target Market(s)
Fishing & seafood industry mainly.
Number of Pages Required
1 page

```html
<!DOCTYPE html>
<html lang="en">
<head>
<meta charset="utf-8">
<title>Polanexa – Gel Ice Packs</title>
<link rel="stylesheet" href="https://fonts.googleapis.com/css2?family=Oswald:wght@500&family=Lato:ital,wght@0,400;0,700;1,400&family=Roboto:wght@400&display=swap">
<style>
:root{
  --brand-blue:#1F419B;
  --nav-blue:#2541a3;
  --slate:#2F4F4F;
  --ink:#2b2b2b;
  --text:#3a3a3a;
  --rule:#b9b9b9;
  --footer-top:#505456;
  --footer-bottom:#34383a;
  --footer-text:#e8e8e8;
  --white:#ffffff;
}
*{box-sizing:border-box;margin:0;padding:0}
html,body{width:980px;height:1200px;overflow:hidden;background:var(--white)}
body{position:relative;font-family:"Roboto",Arial,sans-serif;color:var(--text)}
a{color:inherit;text-decoration:none}

.top-bar{position:absolute;top:0;left:0;width:980px;height:36px;background:var(--white)}
.top-phone{position:absolute;right:108px;top:8px;display:flex;align-items:center;gap:8px;font:italic 700 16px "Lato",sans-serif;color:#222}

.site-header{position:absolute;top:36px;left:0;width:980px;height:78px;background:var(--nav-blue)}
.brand{position:absolute;left:110px;top:20px;display:flex;align-items:center;gap:10px}
.brand-dot{width:26px;height:26px;border-radius:50%;background:var(--white)}
.brand-name{font:700 32px "Lato",sans-serif;color:var(--white);letter-spacing:.5px}
.main-nav{position:absolute;right:108px;top:29px;display:flex;align-items:center;font:400 12.5px "Roboto",sans-serif;color:var(--white)}
.main-nav a{padding:0 7px;border-left:1px solid rgba(255,255,255,.3);line-height:14px}
.main-nav a:last-child{padding-right:0}
.main-nav .home{border-left:none;padding:0 8px 0 0;display:flex}

.hero{position:absolute;top:114px;left:0;width:980px;height:414px;background:linear-gradient(180deg,#8a8d91 0%,#a7aaae 45%,#8e9296 100%)}
.hero-product{position:absolute;left:485px;top:60px;width:415px;height:296px;background:linear-gradient(160deg,#e4dccb 0%,#f3f3f3 55%,#d7dae3 100%);border-radius:6px}
.hero-title{position:absolute;left:107px;top:138px;width:380px;font:500 37px/45px "Oswald",sans-serif;color:var(--white);text-shadow:0 2px 4px rgba(0,0,0,.35)}
.slide-arrow{position:absolute;top:168px;width:31px;height:31px;border-radius:50%;background:var(--white);display:flex;align-items:center;justify-content:center;box-shadow:0 1px 3px rgba(0,0,0,.4)}
.slide-arrow.prev{left:31px}
.slide-arrow.next{left:924px}

.welcome-wrap{position:absolute;top:492px;left:88px;width:804px;height:125px}
.welcome-shadow{position:absolute;inset:0}
.welcome{position:absolute;left:19px;top:11px;width:766px;height:114px;border-radius:10px 10px 0 0;background:linear-gradient(180deg,#5d6062 0%,#3d4042 100%);display:flex;align-items:center}
.welcome-heading{width:248px;padding-left:16px;display:flex;align-items:center;gap:8px;font:400 21px/24px Arial,sans-serif;color:var(--white);border-right:1px solid rgba(255,255,255,.15);height:74px}
.welcome-text{padding:0 22px;font:400 12px/17.5px "Roboto",sans-serif;color:#eee;letter-spacing:.1px}

.column{position:absolute;top:655px;width:361px}
.col-why{left:107px}
.col-benefits{left:513px}
.column-divider{position:absolute;left:489px;top:660px;width:1px;height:250px;background:linear-gradient(180deg,rgba(0,0,0,0),#d6d6d6 20%,#d6d6d6 80%,rgba(0,0,0,0))}
.section-title{display:flex;align-items:center;gap:8px;font:700 18.5px "Lato",sans-serif;color:var(--ink);height:26px}
.section-title .accent{color:var(--brand-blue)}
.title-rule{position:relative;height:1px;background:var(--rule);margin-top:10px}
.title-rule::after{content:"";position:absolute;left:11px;top:0;width:8px;height:8px;background:var(--white);border-right:1px solid var(--rule);border-bottom:1px solid var(--rule);transform:translateY(-4px) rotate(45deg)}
.why-list{list-style:none;margin-top:22px;font:400 12px/20.2px Arial,sans-serif;color:#333}
.why-list li::before{content:"> ";}
.why-copy{margin-top:14px;font:400 11.5px/15.5px Arial,sans-serif;color:#333;padding-left:2px}
.read-more{display:block;margin-top:12px;font:700 11px "Lato",sans-serif;color:var(--brand-blue);padding-left:2px}
.benefit-list{list-style:none;margin-top:20px}
.benefit{padding:0 3px 8px;border-bottom:1px dotted #aaa;margin-bottom:9px}
.benefit:last-child{border-bottom:none;margin-bottom:0;padding-bottom:0}
.benefit h3{font:700 13px "Lato",sans-serif;color:#222;margin-bottom:2px}
.benefit p{font:400 11px/15.5px "Roboto",sans-serif;color:#333}

.site-footer{position:absolute;top:957px;left:0;width:980px;height:243px;background:linear-gradient(180deg,var(--footer-top),var(--footer-bottom));border-top:2px solid #c9c9c9;color:var(--footer-text)}
.footer-col{position:absolute;top:20px}
.footer-col h4{font:700 13.5px "Lato",sans-serif;color:var(--white);padding-bottom:8px;border-bottom:1px solid rgba(255,255,255,.25);display:inline-block;min-width:105px}
.f-nav{left:109px}
.f-nav ul{list-style:none;margin-top:12px;font:400 11px/17.2px "Lato",sans-serif}
.f-nav li::before{content:"› ";font-weight:700}
.f-news{left:260px}
.f-news p{margin-top:13px;font:400 11.5px/16px "Lato",sans-serif;width:140px}
.email-field{margin-top:12px;width:131px;height:25px;border-radius:3px;background:#ececec;font:italic 400 11px/25px "Lato",sans-serif;color:#555;padding-left:7px}
.subscribe{margin-top:9px;width:77px;height:23px;border-radius:3px;background:linear-gradient(180deg,#3f63c9,var(--brand-blue));font:700 12px/23px "Lato",sans-serif;color:var(--white);text-align:center}
.f-testimonial{left:438px;width:258px}
.f-testimonial h4{min-width:175px}
.testimonial-body{margin-top:15px;display:flex;gap:10px}
.client-photo{width:96px;height:96px;border:3px solid #ccc;border-radius:6px;background:linear-gradient(180deg,#9fb3c6 0%,#6d7f90 60%,#2e3238 100%)}
.quote{width:140px;font:italic 400 10.5px/14.5px "Lato",sans-serif}
.quote .mark{font:italic 700 16px "Lato",serif;color:#bbb}
.quote-name{display:block;margin-top:6px;font:700 10.5px "Lato",sans-serif;color:var(--white);font-style:normal}
.f-contact{left:716px;width:160px}
.f-contact h4{min-width:150px}
.contact-row{display:flex;gap:8px;margin-top:14px;font:400 11px/14.5px "Lato",sans-serif}
.contact-row svg{flex:none;margin-top:1px}
.contact-row strong{font-weight:700;color:var(--white)}
.contact-phone{font:700 13px "Lato",sans-serif;color:var(--white)}
.footer-bottom{position:absolute;left:109px;top:190px;width:764px;border-top:1px solid rgba(255,255,255,.18)}
.copyright{position:absolute;left:1px;top:15px;font:400 11px "Lato",sans-serif}
.social{position:absolute;right:4px;top:11px;display:flex;gap:5px}
.social span{width:22px;height:22px;border-radius:50%;border:1.5px solid #ddd}
</style>
</head>
<body>

<div class="top-bar">
  <div class="top-phone">
    <svg width="15" height="15" viewBox="0 0 16 16" aria-hidden="true"><circle cx="8" cy="8" r="7" fill="none" stroke="#1F419B" stroke-width="1.5"/><path d="M5.6 4.3l1.2 1.9-.8.9c.5 1 1.3 1.8 2.3 2.3l.9-.8 1.9 1.2-.6 1.4c-2.8-.3-5.2-2.7-5.5-5.5z" fill="#1F419B"/></svg>
    012-555-0147
  </div>
</div>

<header class="site-header">
  <a class="brand" href="#"><span class="brand-dot"></span><span class="brand-name">polanexa</span></a>
  <nav class="main-nav">
    <a class="home" href="#" aria-label="Home"><svg width="21" height="18" viewBox="0 0 21 18"><path d="M10.5 1L1 9.5h2.7V17h5v-5h3.6v5h5V9.5H20z" fill="#fff"/></svg></a>
    <a href="#">Benefits</a>
    <a href="#">Product Specifications</a>
    <a href="#">Polanexa Applications</a>
    <a href="#">Packaging</a>
    <a href="#">Contact Us</a>
  </nav>
</header>

<section class="hero">
  <div class="hero-bg" role="img" aria-label="Warehouse with pallets of stacked product cartons"></div>
  <div class="hero-product" role="img" aria-label="Open cardboard carton filled with gel ice packs"></div>
  <h1 class="hero-title">Polanexa Ice Packs are effective &amp; reliable ice replacement products</h1>
  <a class="slide-arrow prev" href="#" aria-label="Previous slide"><svg width="10" height="12" viewBox="0 0 10 12"><path d="M7.5 1.5L3 6l4.5 4.5" fill="none" stroke="#333" stroke-width="2.4"/></svg></a>
  <a class="slide-arrow next" href="#" aria-label="Next slide"><svg width="10" height="12" viewBox="0 0 10 12"><path d="M2.5 1.5L7 6l-4.5 4.5" fill="none" stroke="#333" stroke-width="2.4"/></svg></a>
</section>

<section class="welcome-wrap">
  <svg class="welcome-shadow" width="804" height="125" viewBox="0 0 804 125" aria-hidden="true">
    <path d="M8 0H796l-10 125H19z" fill="#2e3032"/>
    <path d="M3 36L19 125V36z" fill="#c9c9c9"/>
    <path d="M801 36L785 125V36z" fill="#c9c9c9"/>
  </svg>
  <div class="welcome">
    <div class="welcome-heading">
      <svg width="36" height="38" viewBox="0 0 36 38" aria-hidden="true"><g stroke="#fff" stroke-width="2.4" fill="none" stroke-linecap="round"><path d="M18 2v34M3.5 10.5l29 17M3.5 27.5l29-17"/><path d="M13 5l5 4 5-4M13 33l5-4 5 4M4 16.5l6-.8-2.2-5.6M32 21.5l-6 .8 2.2 5.6M4 21.5l6 .8-2.2 5.6M32 16.5l-6-.8 2.2-5.6"/></g></svg>
      <h2>WELCOME TO<br>POLANEXA</h2>
    </div>
    <p class="welcome-text">Lorem ipsum dolor sit amet, consectetuer adipiscing elit, sed diam nonummy nibh The euismod tincidunt ut laoreet dolore magna aliquam erat volutpat. Ut wisi enim ad minim veniam, quis nostrud exerci tation ullamcorper suscipit lobortis nisl ut aliquip ex ea is commodo consequat. Duis autem vel eum iriure dolor in hendrerit in vulputate velit esse</p>
  </div>
</section>

<section class="column col-why">
  <h2 class="section-title">
    <svg width="21" height="22" viewBox="0 0 36 38" aria-hidden="true"><g stroke="#1F419B" stroke-width="3" fill="none" stroke-linecap="round"><path d="M18 2v34M3.5 10.5l29 17M3.5 27.5l29-17M13 5l5 4 5-4M13 33l5-4 5 4"/></g></svg>
    WHY USE <span class="accent">POLANEXA?</span>
  </h2>
  <div class="title-rule"></div>
  <ul class="why-list">
    <li>Cost and time saving compared to flake ice</li>
    <li>Polanexa lasts longer &amp; maintains more constant temperature</li>
    <li>Segmented pads provide excellent chill distribution</li>
    <li>High grade film is durable and puncture resistant</li>
    <li>Reuseable and food safe KBRIL Approved</li>
    <li>Packaged ready for quick freezing</li>
  </ul>
  <p class="why-copy">Polanexa Gel-Ice Packs are an effective and reliable ice replacement for chilling products during transit. They have been developed through extensive research and testing.</p>
  <a class="read-more" href="#">Read More &gt;&gt;</a>
</section>

<div class="column-divider"></div>

<section class="column col-benefits">
  <h2 class="section-title">
    <svg width="21" height="22" viewBox="0 0 36 38" aria-hidden="true"><g stroke="#1F419B" stroke-width="3" fill="none" stroke-linecap="round"><path d="M18 2v34M3.5 10.5l29 17M3.5 27.5l29-17M13 5l5 4 5-4M13 33l5-4 5 4"/></g></svg>
    BENEFITS OF <span class="accent">OUR PRODUCTS</span>
  </h2>
  <div class="title-rule"></div>
  <ul class="benefit-list">
    <li class="benefit"><h3>Superior to flake ice</h3><p>Polanexa Gel Ice Packs lower the temperature faster and hold the temperature longer than ice.</p></li>
    <li class="benefit"><h3>Segmented cells are unique to Polanexa.</h3><p>Segmenting a pack enables the even distribution of chill right across the goods and ensures there are no extra cold or extra warm areas</p></li>
    <li class="benefit"><h3>Convenient, clean and efficient</h3><p>Polanexa is very easy to use and is supplied in cartons ready to use once frozen. The cartons have special perforations</p></li>
  </ul>
  <a class="read-more" href="#">Read More &gt;&gt;</a>
</section>

<footer class="site-footer">
  <div class="footer-col f-nav">
    <h4>Navigation</h4>
    <ul>
      <li>Home</li><li>Benefits Product</li><li>Specifications</li><li>Polanexa</li><li>Applications</li><li>Packaging</li><li>Contact Us</li>
    </ul>
  </div>
  <div class="footer-col f-news">
    <h4>Newsletter</h4>
    <p>Lorem ipsum dolor sit amet, consectetuer adipiscing elit,</p>
    <div class="email-field">Email here</div>
    <div class="subscribe">Subscribe</div>
  </div>
  <div class="footer-col f-testimonial">
    <h4>Client Testimonials</h4>
    <div class="testimonial-body">
      <div class="client-photo" role="img" aria-label="Portrait photo of the client"></div>
      <p class="quote"><span class="mark">“</span> Lorem ipsum dolor sit amet consectetuer adipiscing elit a sed diam nonummy nibh This euismod tincidunt ut laoreet volutpat. <span class="mark">”</span><span class="quote-name">Mara Ellison</span></p>
    </div>
  </div>
  <div class="footer-col f-contact">
    <h4>Contact Information</h4>
    <div class="contact-row">
      <svg width="12" height="15" viewBox="0 0 12 15" aria-hidden="true"><path d="M6 0a5.5 5.5 0 00-5.5 5.5C.5 9.5 6 15 6 15s5.5-5.5 5.5-9.5A5.5 5.5 0 006 0zm0 7.7a2.2 2.2 0 110-4.4 2.2 2.2 0 010 4.4z" fill="#fff"/></svg>
      <div><strong>Lorem ipsum dolor sit amet</strong><br>consectetuer adimpisciged diamr nonummy nibh</div>
    </div>
    <div class="contact-row">
      <svg width="13" height="13" viewBox="0 0 16 16" aria-hidden="true"><path d="M3.2 1l2.6 3.3-1.4 1.6c.9 1.9 2.3 3.3 4.2 4.2l1.6-1.4L13.5 11l-1 2.8C6.8 13.5 2.5 9.2 2.2 3.5z" fill="#fff"/></svg>
      <span class="contact-phone">012-555-0147</span>
    </div>
    <div class="contact-row">
      <svg width="13" height="11" viewBox="0 0 14 11" aria-hidden="true"><path d="M1 4L7 .8 13 4v6.2H1z" fill="none" stroke="#fff" stroke-width="1.3"/><path d="M1 4l6 3.6L13 4" fill="none" stroke="#fff" stroke-width="1.3"/></svg>
      <span>info@polanexa.example</span>
    </div>
  </div>
  <div class="footer-bottom">
    <p class="copyright">Copyright 2014&nbsp; polanexa. All Right Reserved</p>
    <div class="social" aria-label="Social links"><span></span><span></span><span></span><span></span></div>
  </div>
</footer>

</body>
</html>
```